Brill Insurance Agency - Business Cards

Hello, I am needing new trendy business cards for our Insurance Agency now that I have a new Logo. I have attached our new logo with several color options along with a business card design that I like. I am leaning towards burgundy and blue colors. I have attached our current business card. I have also attached a headshot of our company president, Martin Vale, that you can use if you wish. Thank you so much in advance for all the wonderful designs!!!!

Target Market(s)

We want to look very professional to potential customers and we also want to look very professional so insurance companies will want to contract with us to sell their product.

Industry/Entity Type

Insurance

Contact Information for Business Card

Martin Vale
mvale@brillagency.com
Business: 555-213-4087
Fax: 555-213-7751
Cell: 555-390-2618
Toll Free: 888-555-0194
42 W Elm Rd Butler, MO 64730
www.brillagency.net

Font styles to use
Serif
Sans Serif

Colors
0355a3
3277b5
f04a50
ec1f27

Requirements
Nice to have
• I love creativity. The more creative and balanced a business card design the more I will like it. I would like the card to be printed horizontally instead of vertically.
Should not have
• My project should not have the Allied Coverage Network logo. It is no longer used in the industry.

```html
<!DOCTYPE html>
<html lang="en">
<head>
<meta charset="utf-8">
<title>Brill Insurance Agency – Business Cards</title>
<link href="https://fonts.googleapis.com/css2?family=Montserrat:wght@600&family=Open+Sans:wght@300;400;700&display=swap" rel="stylesheet">
<style>
  :root {
    --backdrop: #e6e6e4;
    --card-white: #ffffff;
    --card-mist: #ececec;
    --charcoal: #2c2b2e;
    --brand-blue: #1f5a8e;
    --brand-blue-deep: #1a5185;
    --accent-blue: #2d65a0;
    --ink-grey: #4a4a4c;
    --text-light: #ffffff;
    --photo-warm: #c9a999;
    --photo-dark: #2a2a30;
  }
  html, body {
    margin: 0;
    padding: 0;
    width: 1200px;
    height: 1176px;
    overflow: hidden;
    background: var(--backdrop);
  }
  .canvas {
    position: relative;
    width: 1200px;
    height: 1176px;
  }
  .card {
    position: absolute;
    left: 199px;
    width: 782px;
    height: 448px;
    border-radius: 24px;
    overflow: hidden;
    box-shadow: 0 6px 14px rgba(0,0,0,0.28);
  }
  .card--front { top: 108px; background: var(--card-white); }
  .card--back {
    top: 610px;
    background: linear-gradient(180deg, var(--brand-blue) 0%, var(--brand-blue-deep) 100%);
  }

  /* front */
  .front-top {
    position: absolute; left: 0; top: 0; width: 100%; height: 252px;
    background: linear-gradient(180deg, var(--card-white) 0%, var(--card-mist) 100%);
  }
  .brand {
    position: absolute;
    display: flex;
    align-items: center;
    font-family: "Montserrat", sans-serif;
    font-weight: 600;
  }
  .brand__dot { border-radius: 50%; flex: none; }
  .brand__name { line-height: 1.05; }
  .brand__name span { display: block; }
  .brand--front { left: 232px; top: 108px; gap: 22px; color: var(--brand-blue); }
  .brand--front .brand__dot { width: 56px; height: 56px; border: 5px solid var(--ink-grey); box-sizing: border-box; }
  .brand--front .brand__name { font-size: 21px; }
  .brand--front .brand__sub { font-size: 13px; letter-spacing: 3.4px; margin-top: 2px; text-align: center; }

  .headshot {
    position: absolute; left: 538px; top: 30px; width: 244px; height: 222px;
    background: linear-gradient(180deg, var(--photo-warm) 0%, var(--photo-warm) 48%, var(--photo-dark) 75%);
  }
  .info-band {
    position: absolute; left: 0; top: 252px; width: 100%; height: 133px;
    background: var(--charcoal);
  }
  .person {
    position: absolute; right: 436px; top: 282px; text-align: right;
    font-family: "Open Sans", sans-serif;
  }
  .person__name { font-size: 28px; font-weight: 300; color: var(--text-light); letter-spacing: 0.5px; margin: 0; line-height: 1.2; }
  .person__name b { font-weight: 700; }
  .person__role { font-size: 17px; color: var(--accent-blue); margin: 2px 0 0; letter-spacing: 0.3px; }
  .divider {
    position: absolute; left: 390px; top: 272px; width: 2px; height: 93px; background: var(--text-light);
  }
  .contacts {
    position: absolute; left: 408px; top: 272px; margin: 0; padding: 0; list-style: none;
    font-family: "Open Sans", sans-serif; font-size: 18px; color: var(--text-light);
  }
  .contacts li { display: flex; align-items: center; height: 33px; gap: 13px; }
  .contacts svg { width: 18px; height: 18px; flex: none; }
  .address-band {
    position: absolute; left: 0; top: 389px; width: 100%; height: 59px;
    background: var(--brand-blue);
    border-top: 4px solid var(--text-light);
    box-sizing: border-box;
    display: flex; align-items: center; justify-content: center;
    font-family: "Open Sans", sans-serif; font-size: 18px; color: var(--text-light);
  }

  /* back */
  .brand--back { left: 154px; top: 174px; gap: 40px; color: var(--text-light); }
  .brand--back .brand__dot { width: 96px; height: 96px; border: 7px solid var(--text-light); box-sizing: border-box; }
  .brand--back .brand__name { font-size: 32px; }
  .brand--back .brand__sub { font-size: 21px; letter-spacing: 5px; margin-top: 4px; text-align: center; }
</style>
</head>
<body>
<div class="canvas">

  <section class="card card--front" aria-label="Business card front">
    <div class="front-top"></div>
    <div class="brand brand--front">
      <div class="brand__dot"></div>
      <div class="brand__name">
        <span>BRILL INSURANCE</span>
        <span class="brand__sub">AGENCY INC</span>
      </div>
    </div>
    <div class="headshot" role="img" aria-label="Portrait photo of company president Martin Vale in a dark suit"></div>

    <div class="info-band"></div>
    <div class="person">
      <p class="person__name">MARTIN <b>VALE</b></p>
      <p class="person__role">PRESIDENT</p>
    </div>
    <div class="divider"></div>
    <ul class="contacts">
      <li>
        <svg viewBox="0 0 18 18" aria-hidden="true"><path d="M2 7c0-2 3-3 7-3s7 1 7 3v1h-3V6.5H5V8H2z M4 9h10l1 6H3z" fill="#2d65a0"/><circle cx="9" cy="12" r="1.8" fill="#2c2b2e"/></svg>
        <span>000 000 0000</span>
      </li>
      <li>
        <svg viewBox="0 0 18 18" aria-hidden="true"><rect x="1.5" y="4" width="15" height="10" fill="#2d65a0"/><path d="M1.5 4l7.5 6 7.5-6" stroke="#2c2b2e" stroke-width="1.3" fill="none"/></svg>
        <span>youremail@xyz.com</span>
      </li>
      <li>
        <svg viewBox="0 0 18 18" aria-hidden="true"><g fill="none" stroke="#2d65a0" stroke-width="1.3"><circle cx="9" cy="9" r="7"/><ellipse cx="9" cy="9" rx="3" ry="7"/><path d="M2 9h14M3 5.5h12M3 12.5h12"/></g></svg>
        <span>www.yourwebsite.com</span>
      </li>
    </ul>
    <div class="address-band">00, Your address here, City. ST 0000</div>
  </section>

  <section class="card card--back" aria-label="Business card back">
    <div class="brand brand--back">
      <div class="brand__dot"></div>
      <div class="brand__name">
        <span>BRILL INSURANCE</span>
        <span class="brand__sub">AGENCY INC</span>
      </div>
    </div>
  </section>

</div>
</body>
</html>
```